A Web3 (Blockchain) Company need a Web Design

Hi from NineHalfMark.
We need a web design for a Blockchain company focused on infrastructure. We are building infrastructure that make people with non-blockchain knowledge and experience can build blockchain platform/service easier.

Our logo will have bridge/road ambience.
We also think about some blue color.
But please propose your idea.

We want the website to represent us in "Reliable", "Secure", and "Make your blockchain related development easier".

I include sales deck to make you understand more about our business.
We expect the design to be in figma.

```html
<!DOCTYPE html>
<html lang="en">
<head>
<meta charset="utf-8">
<title>NineHalfMark — Bridging you to Web 3.0</title>
<link rel="stylesheet" href="https://fonts.googleapis.com/css2?family=Orbitron:wght@700;800&family=Roboto:wght@300;400;500;700&family=Roboto+Condensed:wght@700&display=swap">
<style>
:root{
  --blue:#1768bd;
  --blue-dark:#0d4e92;
  --blue-light:#4a9ad6;
  --purple:#7b4f93;
  --purple-light:#a584b8;
  --ink:#111418;
  --grey-text:#666b72;
  --soft-bg:#f2f4f5;
  --navy:#0a1836;
  --white:#ffffff;
}
*{box-sizing:border-box;margin:0;padding:0}
html,body{width:1200px;height:4458px;overflow:hidden;background:var(--white)}
body{font-family:"Roboto",sans-serif;color:var(--ink)}
.page{position:relative;width:1200px;height:4458px;overflow:hidden}
.abs{position:absolute}
.display{font-family:"Orbitron",sans-serif;font-weight:800;letter-spacing:1px;text-transform:uppercase}
.accent{color:var(--blue)}
.center{left:0;width:1200px;text-align:center}

/* header */
.brand{left:144px;top:44px;font-family:"Roboto",sans-serif;font-weight:700;font-size:30px;color:var(--blue);letter-spacing:1px}
.brand-dot{display:inline-block;width:12px;height:12px;background:var(--blue);border-radius:50%;margin-right:8px;vertical-align:middle}
.nav{top:56px;left:584px;display:flex;gap:40px;font-size:15px;font-weight:500;color:var(--ink)}

/* hero */
.hero-bg{left:0;top:0;width:1200px;height:1174px}
.hero-title{left:144px;top:170px;font-size:52px;line-height:61px}
.hero-text{left:144px;top:372px;width:340px;font-size:23px;line-height:29px;color:var(--ink)}
.btn{display:flex;align-items:center;justify-content:center;background:var(--purple);color:var(--white);border-radius:30px;font-size:15px;font-weight:500;text-transform:uppercase}
.hero-btn{left:144px;top:499px;width:178px;height:59px}
.hero-art{left:660px;top:104px;width:540px;height:502px;border-radius:40% 10% 30% 50%;background:radial-gradient(circle at 55% 45%,#bcd9ef,#e6f0f8 60%,rgba(255,255,255,0) 75%)}
.dots{left:570px;top:631px;display:flex;gap:6px}
.dots span{width:26px;height:26px;border:1.5px solid #555;border-radius:50%;display:flex;align-items:center;justify-content:center;font-size:14px;color:#555}

/* nutshell */
.nut-diagram{left:144px;top:810px;width:358px;height:302px;border-radius:20px;background:radial-gradient(circle,#dfe6ec,rgba(242,244,245,0) 70%)}
.nut-title{left:599px;top:836px;font-size:40px;line-height:52px}
.nut-text{left:599px;top:955px;width:452px;font-size:13.5px;line-height:25.5px;color:var(--grey-text);text-align:justify}

/* obstacles */
.obs-bg{left:0;top:1174px;width:1200px;height:600px;background:linear-gradient(180deg,#f8fafd,#eef3fa)}
.obs-title{top:1270px;font-size:42px}
.obs-sub{top:1345px;font-size:40px;font-weight:300;color:var(--grey-text);letter-spacing:1px}
.card{width:431px;height:102px;background:var(--white);box-shadow:0 2px 10px rgba(0,0,0,.08);display:flex;align-items:center;padding:0 20px;gap:20px;font-size:17.5px;font-weight:500;line-height:20px}
.card svg{flex:none}

/* pillars */
.pillar{top:1773px;width:398px;height:367px;color:var(--white);display:flex;flex-direction:column;align-items:center;font-family:"Roboto Condensed",sans-serif;font-weight:700;font-size:35px;text-align:center;line-height:37px}
.pillar.blue{background:linear-gradient(180deg,var(--blue-light),var(--blue-dark))}
.pillar.purple{background:linear-gradient(180deg,var(--purple-light),#5e3a78)}
.pillar svg{margin-top:62px}

/* companies */
.comp-title{top:2245px;font-size:42px}
.comp-sub{top:2305px;font-size:40px;font-weight:300;color:var(--grey-text)}
.comp-lead{top:2370px;font-size:17.5px;color:var(--grey-text)}
.logo-row{left:150px;top:2475px;width:900px;display:flex;justify-content:space-between;align-items:center;height:60px}
.logo-row span{font-size:34px;font-weight:700;color:var(--ink)}
.arrow{top:2478px;font-size:52px;font-weight:300;color:#888}

/* team */
.team-bg{left:0;top:2640px;width:1200px;height:576px;background:var(--soft-bg)}
.team-title{top:2716px;font-size:42px}
.team-sub{top:2780px;font-size:13.5px;color:var(--grey-text)}
.avatar{width:184px;height:184px;border-radius:50%;background:linear-gradient(160deg,#c9d3da,#8f9aa3);box-shadow:0 4px 10px rgba(0,0,0,.18);border:5px solid var(--white)}
.member{width:260px}
.member h3{font-size:16px;font-weight:700;text-transform:uppercase}
.member .role{font-size:13.5px;color:var(--blue);margin-top:10px}
.member p{font-size:13.5px;color:var(--grey-text);line-height:21px;margin-top:10px}
.member .more{font-size:14px;font-weight:700;color:var(--purple);margin-top:16px;text-transform:uppercase}
.view-btn{left:511px;top:3082px;width:178px;height:56px}

/* nft */
.nft-bg{left:0;top:3216px;width:1200px;height:760px;background:linear-gradient(180deg,#ffffff,#f1f5fb)}
.nft-title{top:3308px;font-size:42px;line-height:52px}
.nft-sub{top:3436px;font-size:19px;color:var(--grey-text)}
.nft-art{left:144px;top:3498px;width:367px;height:424px;border-radius:16px;background:linear-gradient(160deg,#dce9f7,#6aa6e0 70%,#3f6fc4)}
.nft-list{left:589px;top:3612px;list-style:none;font-size:28px;font-weight:500;line-height:51px}
.nft-list li::before{content:"";display:inline-block;width:14px;height:14px;border-radius:50%;background:var(--purple);margin-right:20px;vertical-align:middle}

/* footer */
.footer-bg{left:0;top:3880px;width:1200px;height:578px}
.contact{top:4071px;width:320px;text-align:center;color:var(--white)}
.contact .icon{width:114px;height:114px;border-radius:50%;margin:0 auto;display:flex;align-items:center;justify-content:center}
.contact h4{font-size:20px;font-weight:700;margin-top:30px}
.contact p{font-size:15px;line-height:24px;margin-top:8px}
.divider{top:4095px;width:1.5px;height:61px;background:#4a5a7a}
.copy{top:4398px;font-size:13px;color:#d6dbe6}
</style>
</head>
<body>
<div class="page">

  <!-- hero background with curve -->
  <svg class="abs hero-bg" viewBox="0 0 1200 1174" aria-hidden="true">
    <rect width="1200" height="1174" fill="#f2f4f5"/>
    <path d="M0,0 H1200 V433 C950,560 750,727 570,727 C330,727 110,650 0,520 Z" fill="#ffffff"/>
    <path d="M0,520 C110,650 330,727 570,727 C750,727 950,560 1200,433" fill="none" stroke="#1768bd" stroke-width="7"/>
  </svg>

  <div class="abs brand"><span class="brand-dot"></span>NINEHALFMARK</div>
  <nav class="abs nav"><span>HOME</span><span>ABOUT</span><span>SERVICES</span><span>NEWS</span><span>CONTACT US</span></nav>

  <div class="abs hero-art" role="img" aria-label="Illustration of a wireframe hand holding glowing blue chain links"></div>
  <h1 class="abs display hero-title">Bridging you to<br><span class="accent">The three point</span><br>Zero</h1>
  <p class="abs hero-text">NineHalfMark helps you to tap into web 3.0 (blockchain based web) technology</p>
  <a class="abs btn hero-btn">Get started</a>
  <div class="abs dots"><span>&#8592;</span><span>&#8594;</span></div>

  <!-- blockchain in a nutshell -->
  <div class="abs nut-diagram" role="img" aria-label="Diagram of blockchain traits: decentralization, immutability, tokenization, distribution and encryption linked in a ring"></div>
  <h2 class="abs display nut-title">Blockchain<br><span class="accent">in a nutshell</span></h2>
  <p class="abs nut-text">Blockchain is a distributed, encrypted,immutable ledger that can alsoincorporates technologies such as asset tokenization and smart contracts. With its decentralized and immutable property, blockchain is a revolutionary technology that addresses problems with fraudulent activities.</p>

  <!-- obstacles -->
  <div class="abs obs-bg"></div>
  <h2 class="abs center display obs-title">Indonesia's web <span class="accent">3.0 project</span></h2>
  <p class="abs center obs-sub">OBSTACLES</p>

  <div class="abs card" style="left:158px;top:1448px">
    <svg width="50" height="46" viewBox="0 0 50 46" fill="none" stroke="#333" stroke-width="2"><rect x="3" y="10" width="42" height="32" rx="4"/><path d="M8 10 L34 3 L37 10"/><rect x="30" y="20" width="16" height="12" rx="3" stroke="#7b4f93"/></svg>
    <span>High effort to educate user about web3 technology especially in web3 wallets</span>
  </div>
  <div class="abs card" style="left:611px;top:1448px">
    <svg width="62" height="50" viewBox="0 0 62 50" fill="none" stroke="#333" stroke-width="2"><circle cx="22" cy="30" r="14" stroke-dasharray="5 3"/><circle cx="22" cy="30" r="6"/><circle cx="46" cy="14" r="10" stroke="#7b4f93"/><path d="M41 14 l4 4 l7 -8" stroke="#7b4f93"/></svg>
    <span>Limited support to develop web 3.0 based projects such as Meadowland and NFT Launcher</span>
  </div>
  <div class="abs card" style="left:158px;top:1574px">
    <svg width="54" height="50" viewBox="0 0 54 50" fill="none" stroke="#333" stroke-width="2"><circle cx="27" cy="10" r="6" stroke="#7b4f93"/><path d="M17 26 a10 8 0 0 1 20 0" stroke="#7b4f93"/><circle cx="12" cy="33" r="5"/><path d="M3 47 a9 8 0 0 1 18 0"/><circle cx="42" cy="33" r="5"/><path d="M33 47 a9 8 0 0 1 18 0"/></svg>
    <span>Limited availability of web<br>3.0 developer</span>
  </div>
  <div class="abs card" style="left:611px;top:1574px">
    <svg width="54" height="54" viewBox="0 0 54 54" fill="none" stroke="#333" stroke-width="2"><circle cx="27" cy="27" r="23"/><path d="M27 12 V29 H16" stroke="#7b4f93"/></svg>
    <span>High latency due to lack of Indonesia based RPC nodes</span>
  </div>

  <!-- pillars -->
  <div class="abs pillar blue" style="left:0">
    <svg width="160" height="160" viewBox="0 0 160 160" fill="none" stroke="#fff" stroke-width="5"><circle cx="80" cy="36" r="24"/><path d="M68 36 l9 9 l16 -18"/><path d="M10 80 L45 60 L80 78 L115 60 L150 80 L110 130 L80 145 L50 130 Z"/></svg>
    <div style="margin-top:22px">Reliable</div>
  </div>
  <div class="abs pillar purple" style="left:400px">
    <svg width="120" height="112" viewBox="0 0 120 112" fill="none" stroke="#fff" stroke-width="5" style="margin-top:58px"><rect x="8" y="8" width="22" height="22"/><rect x="90" y="8" width="22" height="22"/><rect x="8" y="82" width="22" height="22"/><rect x="90" y="82" width="22" height="22"/><rect x="42" y="40" width="36" height="32"/><path d="M30 19 H50 V40 M90 19 H70 V40 M30 93 H50 V72 M90 93 H70 V72"/></svg>
    <div style="margin-top:22px">Make your<br>blockchain related<br>development easier</div>
  </div>
  <div class="abs pillar blue" style="left:802px">
    <svg width="180" height="170" viewBox="0 0 180 170" fill="none" stroke="#fff" stroke-width="5"><path d="M90 6 L130 20 V60 C130 90 110 105 90 115 C70 105 50 90 50 60 V20 Z"/><path d="M72 60 l13 13 l24 -26"/><rect x="6" y="105" width="26" height="55" rx="3"/><path d="M32 115 H80 C95 115 100 128 85 130 H60 M32 150 H110 L172 112 C165 100 150 102 140 110 L110 128"/></svg>
    <div style="margin-top:14px">Secure</div>
  </div>

  <!-- companies -->
  <h2 class="abs center display comp-title">Companies <span class="accent">on</span></h2>
  <p class="abs center comp-sub">WEB 3.0</p>
  <p class="abs center comp-lead">As for now, big companies are already entering web 3.0 and creating revenue</p>
  <div class="abs arrow" style="left:94px">&#8249;</div>
  <div class="abs arrow" style="left:1078px">&#8250;</div>
  <div class="abs logo-row">
    <span>Hourly</span><span>Veloce</span><span>Stridewell</span><span>Duo&amp;Co</span><span>Swiftmark</span>
  </div>

  <!-- team -->
  <div class="abs team-bg"></div>
  <h2 class="abs center display team-title">Meet our <span class="accent">teams</span></h2>
  <p class="abs center team-sub">we will help you to tap in web3 ecosystems</p>

  <div class="abs avatar" style="left:163px;top:2857px" role="img" aria-label="Portrait photo of the CEO"></div>
  <div class="abs member" style="left:372px;top:2874px">
    <h3>Raka Wiradana</h3>
    <div class="role">CEO</div>
    <p>Building infrastructure for digital billing in Indonesia since 2005</p>
    <div class="more">Read more</div>
  </div>
  <div class="abs avatar" style="left:635px;top:2857px" role="img" aria-label="Portrait photo of the CTO"></div>
  <div class="abs member" style="left:843px;top:2874px">
    <h3>Bayu Pratama</h3>
    <div class="role">CTO</div>
    <p>Ledgerline 30 under 30 Asia<br>Indonesia Tech Rockstar</p>
    <div class="more">Read more</div>
  </div>
  <a class="abs btn view-btn">View more</a>

  <!-- nft starter -->
  <div class="abs nft-bg"></div>
  <h2 class="abs center display nft-title">NineHalfMark<br>NFT <span class="accent">starter</span></h2>
  <p class="abs center nft-sub">create and launch your NFT with ease</p>
  <div class="abs nft-art" role="img" aria-label="Illustration of a person painting among floating media windows on an NFT platform"></div>
  <ul class="abs nft-list">
    <li>NFT Minting, Transfer and Burn</li>
    <li>As easy as image upload</li>
    <li>Customizable rule and use case</li>
    <li>Supporting Soul-Bound Token</li>
  </ul>

  <!-- footer -->
  <svg class="abs footer-bg" viewBox="0 0 1200 578" aria-hidden="true">
    <defs><linearGradient id="navyFade" x1="0" y1="0" x2="0" y2="1"><stop offset="0" stop-color="#10265a"/><stop offset="1" stop-color="#0a1836"/></linearGradient></defs>
    <path d="M0,270 C300,80 800,20 1200,40 V578 H0 Z" fill="url(#navyFade)"/>
    <path d="M0,270 C300,80 800,20 1200,40" fill="none" stroke="#1768bd" stroke-width="7"/>
  </svg>

  <div class="abs contact" style="left:127px">
    <div class="icon" style="background:var(--purple)"><svg width="40" height="52" viewBox="0 0 40 52"><path d="M20 2 C9 2 2 10 2 20 C2 33 20 50 20 50 C20 50 38 33 38 20 C38 10 31 2 20 2 Z" fill="#fff"/><circle cx="20" cy="19" r="7" fill="#7b4f93"/></svg></div>
    <h4>Address</h4>
    <p>123,Sed ut perspiciatis unde<br>omnis iste natus</p>
  </div>
  <div class="abs divider" style="left:450px"></div>
  <div class="abs contact" style="left:444px">
    <div class="icon" style="background:var(--blue)"><svg width="48" height="48" viewBox="0 0 48 48"><path d="M10 4 L18 4 L21 14 L15 18 C18 25 23 30 30 33 L34 27 L44 30 L44 38 C44 42 40 45 36 44 C18 40 6 28 4 12 C3 8 6 4 10 4 Z" fill="#fff"/></svg></div>
    <h4>Phone</h4>
    <p style="font-size:19px">+1 555 010 2040</p>
  </div>
  <div class="abs divider" style="left:764px"></div>
  <div class="abs contact" style="left:759px">
    <div class="icon" style="background:var(--purple)"><svg width="52" height="38" viewBox="0 0 52 38" fill="none" stroke="#fff" stroke-width="3"><rect x="2" y="2" width="48" height="34"/><path d="M2 2 L26 22 L50 2 M2 36 L20 18 M50 36 L32 18"/></svg></div>
    <h4>Email</h4>
    <p>info@ninehalfmark.com</p>
  </div>

  <p class="abs center copy">&copy; 2022 NineHalfMark. All rights reserved.Privacy | Terms of Use</p>
</div>
</body>
</html>
```